Business Card

Need business cards and small flyers for a musical band

Target Market(s)

Promoters, clients seeking to hire a Latin band

Industry/Entity Type

Business

Requirements
Must have
• The name of the band is Orchestra Brisa so want to have the background with a fire design, with black card and the name of the band in RED, maybe a combination of Red with some yellow. See attached idea.
Nice to have
• See attached files for some ideas.

```html
<!DOCTYPE html>
<html lang="en">
<head>
<meta charset="utf-8">
<title>Orchestra Brisa – Business Card</title>
<link href="https://fonts.googleapis.com/css2?family=Didact+Gothic&family=Arimo:wght@700&display=swap" rel="stylesheet">
<style>
  :root {
    --page-light: #f4f4f4;
    --page-dark: #bdbdbd;
    --ember-dark: #3a1408;
    --ember-mid: #8a2e0e;
    --flame-orange: #e0701c;
    --flame-yellow: #f7c44a;
    --band-white: rgba(255, 245, 235, 0.42);
    --band-line: rgba(255, 245, 235, 0.28);
    --brand-red: #d6221c;
  }
  * { margin: 0; padding: 0; box-sizing: border-box; }
  html, body {
    width: 1200px;
    height: 900px;
    overflow: hidden;
  }
  body {
    background: radial-gradient(ellipse at 50% 35%, var(--page-light) 0%, #dcdcdc 60%, var(--page-dark) 100%);
    position: relative;
    font-family: "Didact Gothic", "Century Gothic", sans-serif;
  }
  .business-card {
    position: absolute;
    left: 110px;
    top: 170px;
    width: 980px;
    height: 560px;
    overflow: hidden;
    box-shadow: 0 10px 28px rgba(0, 0, 0, 0.35);
  }
  .fire-backdrop {
    position: absolute;
    inset: 0;
    background:
      radial-gradient(ellipse at 55% 40%, var(--flame-yellow) 0%, rgba(247, 196, 74, 0) 28%),
      radial-gradient(ellipse at 30% 30%, rgba(240, 150, 50, 0.85) 0%, rgba(240, 150, 50, 0) 35%),
      radial-gradient(ellipse at 80% 25%, rgba(245, 170, 60, 0.8) 0%, rgba(245, 170, 60, 0) 30%),
      radial-gradient(ellipse at 65% 75%, rgba(224, 112, 28, 0.8) 0%, rgba(224, 112, 28, 0) 40%),
      radial-gradient(ellipse at 15% 80%, rgba(138, 46, 14, 0.9) 0%, rgba(138, 46, 14, 0) 45%),
      linear-gradient(160deg, var(--ember-mid) 0%, var(--flame-orange) 45%, var(--ember-mid) 75%, var(--ember-dark) 100%);
  }
  .band {
    position: absolute;
    left: 0;
    right: 0;
    background: var(--band-white);
  }
  .band--title { top: 165px; height: 88px; }
  .band--thin { top: 265px; height: 34px; background: var(--band-line); }
  .band--contact { top: 330px; height: 56px; background: var(--band-line); }
  .band--name { top: 400px; height: 84px; }
  .band-name {
    position: absolute;
    top: 173px;
    left: 0;
    right: 0;
    text-align: center;
    font-size: 66px;
    color: var(--brand-red);
    letter-spacing: 0.5px;
  }
  .phone {
    position: absolute;
    top: 296px;
    right: 90px;
    display: flex;
    align-items: center;
    gap: 8px;
    font-family: "Arimo", Arial, sans-serif;
    font-weight: 700;
    font-size: 24px;
    color: var(--brand-red);
  }
  .phone-icon { width: 16px; height: 16px; }
  .person {
    position: absolute;
    left: 150px;
    top: 408px;
    color: var(--brand-red);
  }
  .person-name {
    font-size: 34px;
    line-height: 1.05;
  }
  .person-role {
    font-size: 30px;
    line-height: 1.05;
    padding-left: 32px;
    color: #c02a20;
  }
</style>
</head>
<body>
  <section class="business-card">
    <div class="fire-backdrop" role="img" aria-label="Photograph of roaring orange and yellow flames filling the card background"></div>
    <div class="band band--title"></div>
    <div class="band band--thin"></div>
    <div class="band band--contact"></div>
    <div class="band band--name"></div>

    <h1 class="band-name">Orchestra Brisa</h1>

    <p class="phone">
      <svg class="phone-icon" viewBox="0 0 24 24" aria-hidden="true">
        <path fill="#d6221c" d="M6.6 10.8a15.1 15.1 0 0 0 6.6 6.6l2.2-2.2a1 1 0 0 1 1-.25 11.4 11.4 0 0 0 3.6.57 1 1 0 0 1 1 1V20a1 1 0 0 1-1 1A17 17 0 0 1 3 4a1 1 0 0 1 1-1h3.5a1 1 0 0 1 1 1c0 1.25.2 2.45.57 3.57a1 1 0 0 1-.25 1z"/>
      </svg>
      (555) 210-7384
    </p>

    <div class="person">
      <p class="person-name">Rafael Quintero</p>
      <p class="person-role">musical director</p>
    </div>
  </section>
</body>
</html>
```